Business Card Design

We're a new real estate investment company based out of West Palm Beach Florida. We buy distressed properties to fix and flip. We want the color scheme of the card to match the colors of our logo which is black and gold. We encourage all designers to be creative with the design of the card. We are not looking for a bland, boring, traditional business card. Please use legible fonts for the text as well.

Target Market(s)

Home owners, and Real Estate Investors.

Industry/Entity Type

Real Estate

Contact Information for Business Card

Tavis Quembry
Real Estate Investor

HARBOR OAKWELL, LLC
7148 S. CANFIELD ROAD
SUITE 28
WEST PALM BEACH, FL. 33562
OFFICE: 1-800-555-0193
FAX: 1-888-555-0147
EMAIL: tavis@harboroakwell.example
www.harboroakwell.example

Requirements
Must have
• PLACE THESE WORDS IN BIG BOLD PRINT ON BOTH SIDES OF THE DESIGN:

WE BUY HOUSES WITH CASH!

```html
<!DOCTYPE html>
<html lang="en">
<head>
<meta charset="utf-8">
<title>Harbor Oakwell – Business Card</title>
<link rel="stylesheet" href="https://fonts.googleapis.com/css2?family=Open+Sans:wght@400;600;700;800&display=swap">
<style>
  :root {
    --gold: #f0cb0a;
    --gold-deep: #d9b400;
    --ink: #111111;
    --text: #1c1c1c;
    --paper: #ffffff;
    --backdrop: #e9e6e2;
    --rule: #2a2a2a;
  }
  * { box-sizing: border-box; margin: 0; padding: 0; }
  html, body { width: 1200px; height: 1140px; overflow: hidden; }
  body {
    background: var(--backdrop);
    font-family: "Open Sans", Arial, sans-serif;
    color: var(--text);
    position: relative;
  }
  .card {
    position: absolute;
    width: 894px;
    height: 511px;
    background: var(--paper);
    box-shadow: 0 6px 18px rgba(0,0,0,.18);
    overflow: hidden;
  }
  .card--front { left: 36px; top: 44px; }
  .card--back { left: 276px; top: 588px; }

  .brand-mark {
    position: absolute;
    display: flex;
    align-items: center;
    gap: 12px;
    font-weight: 700;
    color: var(--ink);
    line-height: 1;
  }
  .brand-mark__square { background: var(--gold); flex: none; }
  .card--front .brand-mark { left: 64px; top: 110px; font-size: 27px; }
  .card--front .brand-mark__square { width: 44px; height: 44px; }
  .card--back .brand-mark {
    left: 0; right: 0; top: 150px; justify-content: center;
    font-size: 50px; gap: 20px;
  }
  .card--back .brand-mark__square { width: 76px; height: 76px; }

  .headline {
    position: absolute;
    font-weight: 800;
    color: var(--ink);
    line-height: 1.1;
    white-space: nowrap;
  }
  .card--front .headline { left: 64px; top: 40px; font-size: 30px; }
  .card--back .headline {
    left: 0; right: 0; top: 290px; text-align: center; font-size: 42px;
  }
  .headline__accent { color: var(--gold-deep); }

  .contact { position: absolute; left: 76px; top: 258px; }
  .contact__row { display: flex; align-items: center; gap: 22px; font-size: 21px; line-height: 34px; }
  .contact__item { display: flex; align-items: center; gap: 6px; }
  .contact__icon { width: 18px; height: 18px; flex: none; }
  .company { position: absolute; left: 76px; top: 340px; line-height: 29px; }
  .company__name { font-size: 19px; font-weight: 700; }
  .company__line { font-size: 17px; }

  .portrait {
    position: absolute; left: 620px; top: 133px; width: 274px; height: 310px;
    background: linear-gradient(180deg, #e8e8ea 0%, #3a3a40 55%, #15151a 100%);
  }
  .front-rule { position: absolute; left: 0; right: 0; top: 443px; height: 3px; background: var(--rule); }
  .band {
    position: absolute; left: 0; right: 0; top: 452px; height: 59px;
    background: linear-gradient(180deg, var(--gold), var(--gold-deep));
    display: flex; align-items: center; justify-content: space-between;
    padding: 0 16px 0 84px;
  }
  .band__web { font-size: 21px; font-weight: 600; letter-spacing: .5px; color: var(--ink); }
  .band__person { font-size: 19px; color: var(--ink); }
  .band__name { font-size: 25px; font-weight: 700; }

  .back-web {
    position: absolute; left: 0; right: 0; top: 434px; text-align: center;
    font-size: 27px; font-weight: 600; letter-spacing: 1.5px; color: var(--text);
  }
</style>
</head>
<body>
  <section class="card card--front" aria-label="Card front">
    <p class="headline">WE BUY HOUSES WITH <span class="headline__accent">CASH!</span></p>
    <div class="brand-mark"><span class="brand-mark__square"></span>HARBOR OAKWELL</div>

    <div class="contact">
      <div class="contact__row">
        <span class="contact__item">
          <svg class="contact__icon" viewBox="0 0 20 20" aria-hidden="true"><circle cx="10" cy="10" r="9" fill="var(--gold)"/><path d="M6.5 5.5l2 0 1 3-1.3 1a6 6 0 0 0 2.6 2.6l1-1.3 3 1v2a1.5 1.5 0 0 1-1.5 1.5A9 9 0 0 1 5 7a1.5 1.5 0 0 1 1.5-1.5z" fill="#7a6200"/></svg>
          1-800-555-0193
        </span>
        <span class="contact__item">
          <svg class="contact__icon" viewBox="0 0 20 20" aria-hidden="true"><rect x="3" y="8" width="14" height="8" rx="1.5" fill="var(--gold)"/><rect x="6" y="3" width="8" height="6" fill="var(--gold-deep)"/></svg>
          1-888-555-0147
        </span>
      </div>
      <div class="contact__row">
        <span class="contact__item">
          <svg class="contact__icon" viewBox="0 0 20 20" aria-hidden="true"><rect x="2" y="5" width="16" height="11" rx="1.5" fill="var(--gold)"/><path d="M2 6l8 6 8-6" fill="none" stroke="#7a6200" stroke-width="1.4"/></svg>
          tavis@harboroakwell.example
        </span>
      </div>
    </div>

    <div class="company">
      <p class="company__name">HARBOR OAKWELL, LLC</p>
      <p class="company__line">7148 S. CANFIELD ROAD</p>
      <p class="company__line">SUITE 28 WEST PALM BEACH, FL. 33562</p>
    </div>

    <div class="portrait" role="img" aria-label="Portrait photo of Tavis Quembry in a dark suit"></div>
    <div class="front-rule"></div>
    <div class="band">
      <span class="band__web">www.harboroakwell.example</span>
      <span class="band__person"><span class="band__name">Tavis Quembry,</span> Real Estate Investor</span>
    </div>
  </section>

  <section class="card card--back" aria-label="Card back">
    <div class="brand-mark"><span class="brand-mark__square"></span>HARBOR OAKWELL</div>
    <p class="headline">WE BUY HOUSES WITH <span class="headline__accent">CASH!</span></p>
    <p class="back-web">www.harboroakwell.example</p>
  </section>
</body>
</html>
```